Real Estate Search Site Re-Design of 2 Pages

Looking for designs to optimize 2 pages of our current site design. Our site allows users to find properties to purchase or rent.

Basically there are 4 panes
1. The top red one where you actually type in what you''re looking for.
2. The map pane that shows the properties
3. The scrollable results pane.
4. Property details pane.

A typical search would go like this:
1. User fills in their search criteria in the top pane in red. Clicks Find Homes
2. Site updates the map with properties plotted that fit the criteria. Site also populates the results pane at the bottom. Site shows the most newest property that fits the search criteria on the right.
3. User will scroll through the results pane or the map and click a property.
4. Site will update the property details pane with information on the selected property.

Search/Results Page
This main page needs a search form area, a results area, an area to display details of a property selected, a map to show results, and an area to display a real estate agent's information. The design must be full-screen to use all the space on the screen. All information should fit on a 1366x768 screen size. Please see sample screen shot.

Property Details Page
This one can be fixed width of 978px. This page needs all the elements that are displayed in the sample PNG file. Ideally, we want to be able to see all important information without scrolling on a 1366x768 screen. The important information in this size are Pictures with controls, address, bedrooms, bathrooms, square feet, square feet of the lot, days on market, agent information, and buttons to request a showing or get more information.

Our Goal:
Our goal is to get create a different way to display the data in an effective way. We want different ways to show the search results, maybe a vertical, scrolling list of property information with pictures. Or even a horizontal scrolling results pane. It must contain:

1. A map of the results
2. A way to scroll through the search results (like we have currently in case someone wants to search/sort bedrooms or square footage)
3. A way to view details of the property
4. A way to display agent information/picture

There's a lot of good design work coming through. Thank you.

Perhaps review some other real estate sales sites for ideas on pane configuration. Example site links:
http://www.brovenly.com/homes/for_sale/?gclid=QmTr8k2-xw7HJd3P9Lq0VnE5ZB (brovenly.com)
http://www.pemoda.com/?sem=1.2.1.5.7.1.0.14&gclid=ZKwp42h-ty8NGRmX5BqeuLcHTD (Pemoda.com)
http://www.quivrent.com/map_search/results/i/ (quivrent.com)

Our goal for the redesign is to display the data in a more effective way. Either with a better flow, more pictures, more information, smoother search process. Please see the updated brief for details. The main idea is to show the data in the most effective way possible.

Project Deadline Extended
Reason: Still looking at different ideas for the search results. We are still open for fresh ideas.

Industry/Entity Type

Real Estate

Font styles to use
Sans Serif

Colors
eb1f27

```html
<!DOCTYPE html>
<html lang="en">
<head>
<meta charset="utf-8">
<title>Property Search</title>
<link href="https://fonts.googleapis.com/css2?family=Roboto:wght@400;500;700&display=swap" rel="stylesheet">
<style>
:root{
  --brand:#eb1f27;
  --brand-dark:#b5121a;
  --accent:#ff5a1f;
  --panel:rgba(20,20,20,.88);
  --panel-solid:#2a2a2a;
  --text-light:#ffffff;
  --text-muted:#cfcfcf;
  --map-base:#ece9e1;
  --row-alt:#f4f4f4;
  --row-line:#e2e2e2;
  --ink:#444;
}
*{box-sizing:border-box;margin:0;padding:0}
html,body{width:1200px;height:674px;overflow:hidden}
body{font-family:'Roboto',Arial,sans-serif;background:#fff;position:relative;color:var(--ink)}

.site-header{position:absolute;left:0;top:0;width:1200px;height:62px;background:linear-gradient(var(--brand),#d8141c);}
.brand-box{position:absolute;left:26px;top:11px;width:106px;height:40px;background:#fff;border-radius:2px;color:var(--brand);font-weight:700;font-size:28px;display:flex;align-items:center;justify-content:center;letter-spacing:1px}
.main-nav{position:absolute;top:0;left:350px;height:62px;display:flex;align-items:center;gap:0}
.main-nav a{color:#fff;text-decoration:none;font-weight:500;font-size:16px;margin-right:50px}
.lang-select{position:absolute;left:1090px;top:18px;width:82px;height:26px;background:var(--accent);color:#fff;font-size:14px;border-radius:2px;display:flex;align-items:center;padding-left:10px;gap:8px;border:1px solid #d94300}

.map-area{position:absolute;left:0;top:62px;width:1200px;height:413px;background:linear-gradient(135deg,#eeebe3,#e4e1d4 50%,#ecebe4);}
.map-pin{position:absolute;width:26px;height:32px}

.search-panel{position:absolute;left:26px;top:90px;width:282px;height:223px;background:var(--panel);color:#fff;border-radius:2px}
.search-panel h2{font-size:15px;font-weight:700;text-align:center;padding:11px 0 0;height:38px;border-bottom:1px solid #555}
.field-row{position:absolute;left:0;display:flex;align-items:center;font-size:14px}
.field-label{position:absolute;left:12px}
.input{position:absolute;height:27px;background:#fff;border-radius:2px;font-size:12px;color:#aaa;display:flex;align-items:center;padding-left:8px}
.select::after{content:"";position:absolute;right:0;top:0;width:26px;height:27px;background:#e6e6e6;border-left:1px solid #ccc}
.select::before{content:"";position:absolute;right:8px;top:11px;border:5px solid transparent;border-top:6px solid #777;z-index:1}
.search-btn{position:absolute;left:230px;top:54px;width:34px;height:27px;background:var(--accent);border-radius:2px}

.agent-card{position:absolute;left:26px;top:348px;width:282px;height:127px;background:var(--panel);color:#fff;border-radius:2px 2px 0 0}
.agent-photo{position:absolute;left:18px;top:16px;width:74px;height:88px;border:2px solid #fff;background:linear-gradient(#d9cfc6,#b8a99b)}
.agent-info{position:absolute;left:109px;top:12px;line-height:19px;font-size:13px}
.agent-role{color:var(--accent);font-size:14px;font-weight:500}
.agent-name{font-size:16px;font-weight:700;margin:2px 0 2px}

.listing-panel{position:absolute;left:911px;top:102px;width:261px;height:332px;background:var(--panel);color:#fff;border-radius:2px;padding:0 12px}
.listing-title{font-size:12px;font-weight:500;padding-top:14px;height:38px}
.listing-photo{position:relative;width:228px;height:130px;border:3px solid #fff;background:linear-gradient(#9ec8ea 0%,#bcd6e8 35%,#c98a6a 36%,#d9b08f 55%,#4f8a3c 70%,#2e6a2a 100%)}
.photo-bar{position:absolute;left:0;bottom:0;width:100%;height:20px;background:rgba(0,0,0,.45);font-size:12px;display:flex;align-items:center;justify-content:space-between;padding:0 8px}
.listing-facts{margin-top:13px;font-size:12px;line-height:19.5px}
.listing-actions{display:flex;gap:10px;margin-top:9px}
.btn{height:28px;font-size:12px;font-weight:500;display:flex;align-items:center;justify-content:center;border-radius:2px;color:#fff}
.btn-details{width:101px;background:var(--brand)}
.btn-home{width:88px;background:var(--accent)}
.listing-credit{font-size:12px;margin-top:15px}

.results{position:absolute;left:0;top:475px;width:1200px;height:167px;overflow:hidden}
.results table{width:1182px;border-collapse:collapse;table-layout:fixed}
.results th{height:31px;background:linear-gradient(#5a5a5a,#2e2e2e);color:#fff;font-weight:400;font-size:15px}
.results td{height:27px;font-size:13px;text-align:center;border-right:1px solid var(--row-line);border-bottom:1px solid var(--row-line)}
.results td:first-child{text-align:left;padding-left:26px}
.results tr:nth-child(even) td{background:var(--row-alt)}
.sort-up{display:inline-block;margin-left:6px;border:5px solid transparent;border-bottom:7px solid #fff;vertical-align:3px}
.scroll-track{position:absolute;right:0;top:31px;width:18px;height:136px;background:#f0f0f0}
.scroll-thumb{position:absolute;left:3px;top:24px;width:12px;height:50px;background:var(--brand);border-radius:3px}

.site-footer{position:absolute;left:0;top:642px;width:1200px;height:32px;background:#a5050a;color:#fff;font-size:11px;display:flex;align-items:center;padding-left:25px}
.social{position:absolute;right:18px;top:10px;display:flex;gap:12px}
.social span{width:12px;height:12px;border-radius:50%;background:#fff}
</style>
</head>
<body>

<header class="site-header">
  <div class="brand-box">LOGO</div>
  <nav class="main-nav">
    <a href="#">COMMUNITIES</a>
    <a href="#">LOCATIONS</a>
    <a href="#">CONTACT</a>
  </nav>
  <div class="lang-select">English
    <svg width="12" height="8" viewBox="0 0 12 8"><path d="M0 0h12L6 7z" fill="#fff"/></svg>
  </div>
</header>

<section class="map-area" role="img" aria-label="Road map of the search region with property markers">
  <svg class="map-pin" style="left:377px;top:56px" viewBox="0 0 26 32"><path d="M13 0a13 13 0 0 1 13 13c0 9-13 19-13 19S0 22 0 13A13 13 0 0 1 13 0z" fill="#e0151d"/><path d="M7 14l6-6 6 6v5H7z" fill="#fff"/></svg>
  <svg class="map-pin" style="left:640px;top:103px" viewBox="0 0 26 32"><path d="M13 0a13 13 0 0 1 13 13c0 9-13 19-13 19S0 22 0 13A13 13 0 0 1 13 0z" fill="#e0151d"/><path d="M7 14l6-6 6 6v5H7z" fill="#fff"/></svg>
  <svg class="map-pin" style="left:756px;top:71px" viewBox="0 0 26 32"><path d="M13 0a13 13 0 0 1 13 13c0 9-13 19-13 19S0 22 0 13A13 13 0 0 1 13 0z" fill="#ff6a1f"/><rect x="8" y="7" width="10" height="12" fill="#fff"/></svg>
  <svg class="map-pin" style="left:510px;top:178px" viewBox="0 0 26 32"><path d="M13 0a13 13 0 0 1 13 13c0 9-13 19-13 19S0 22 0 13A13 13 0 0 1 13 0z" fill="#e0151d"/><rect x="8" y="7" width="10" height="12" fill="#fff"/></svg>
  <svg class="map-pin" style="left:793px;top:202px" viewBox="0 0 26 32"><path d="M13 0a13 13 0 0 1 13 13c0 9-13 19-13 19S0 22 0 13A13 13 0 0 1 13 0z" fill="#e0151d"/><rect x="8" y="7" width="10" height="12" fill="#fff"/></svg>
  <svg class="map-pin" style="left:565px;top:264px" viewBox="0 0 26 32"><path d="M13 0a13 13 0 0 1 13 13c0 9-13 19-13 19S0 22 0 13A13 13 0 0 1 13 0z" fill="#ff6a1f"/><path d="M7 14l6-6 6 6v5H7z" fill="#fff"/></svg>
  <svg class="map-pin" style="left:364px;top:336px" viewBox="0 0 26 32"><path d="M13 0a13 13 0 0 1 13 13c0 9-13 19-13 19S0 22 0 13A13 13 0 0 1 13 0z" fill="#ff6a1f"/><rect x="8" y="7" width="10" height="12" fill="#fff"/></svg>
</section>

<section class="search-panel">
  <h2>SEARCH PROPERTY BY</h2>
  <span class="field-label" style="top:62px">Location:</span>
  <div class="input" style="left:78px;top:54px;width:147px">Alhambra</div>
  <div class="search-btn">
    <svg width="34" height="27" viewBox="0 0 34 27"><circle cx="16" cy="12" r="5" fill="none" stroke="#fff" stroke-width="2"/><path d="M19.5 15.5l4 4" stroke="#fff" stroke-width="2.5"/></svg>
  </div>
  <span class="field-label" style="top:100px">Type:</span>
  <div class="input select" style="left:78px;top:95px;width:186px">Condo / Townhouse</div>
  <span class="field-label" style="top:143px">Price:</span>
  <div class="input select" style="left:78px;top:138px;width:77px">$500k</div>
  <span class="field-label" style="left:165px;top:143px">to</span>
  <div class="input select" style="left:187px;top:138px;width:77px">$ 1 M</div>
  <span class="field-label" style="top:184px">Beds:</span>
  <div class="input select" style="left:78px;top:179px;width:66px">3+</div>
  <span class="field-label" style="left:152px;top:184px">Baths</span>
  <div class="input select" style="left:198px;top:179px;width:66px">2+</div>
</section>

<aside class="agent-card">
  <div class="agent-photo" role="img" aria-label="Portrait of the buyer's agent"></div>
  <div class="agent-info">
    <div class="agent-role">Buyes's Agent</div>
    <div class="agent-name">Lena Hollis</div>
    <div>(555) 014-2290</div>
    <div>lena@hollisrealty.net</div>
    <div>BRE #04821937</div>
  </div>
</aside>

<aside class="listing-panel">
  <div class="listing-title">482 Alder Crest Lane Maple Heights</div>
  <div class="listing-photo" role="img" aria-label="Exterior photo of a two-storey house with garden">
    <div class="photo-bar">
      <svg width="8" height="12" viewBox="0 0 8 12"><path d="M7 1L2 6l5 5" stroke="#fff" stroke-width="1.5" fill="none"/></svg>
      <span>1/32</span>
      <svg width="8" height="12" viewBox="0 0 8 12"><path d="M1 1l5 5-5 5" stroke="#fff" stroke-width="1.5" fill="none"/></svg>
    </div>
  </div>
  <div class="listing-facts">
    <div>$2,388,000 Listing Price</div>
    <div>3 Beds &nbsp;&nbsp; 3 Baths &nbsp;&nbsp; Built in 2014</div>
    <div>3,866 Sq. Ft ($656/Sq. Ft.) &nbsp;9,866 Sq. Ft. Lot</div>
    <div>25 Days on Market (#AR1344445)</div>
  </div>
  <div class="listing-actions">
    <div class="btn btn-details">VIEW DETAILS</div>
    <div class="btn btn-home">VIEW HOME</div>
  </div>
  <div class="listing-credit">Courtesy Of Brightgate Realty Group</div>
</aside>

<section class="results">
  <table>
    <colgroup>
      <col style="width:214px"><col style="width:152px"><col style="width:156px"><col style="width:156px"><col style="width:108px"><col style="width:132px"><col style="width:132px"><col style="width:132px">
    </colgroup>
    <thead>
      <tr><th>Address<i class="sort-up"></i></th><th>City<i class="sort-up"></i></th><th>Price<i class="sort-up"></i></th><th>Beds<i class="sort-up"></i></th><th>Baths<i class="sort-up"></i></th><th>Sq. Ft<i class="sort-up"></i></th><th>$/Sq.Ft.<i class="sort-up"></i></th><th>Days<i class="sort-up"></i></th></tr>
    </thead>
    <tbody>
      <tr><td>482 Alder Crest Lane</td><td>Maple Heights</td><td>$ 1,200,000</td><td>4</td><td>2.5</td><td>1,814</td><td>$ 765</td><td>5</td></tr>
      <tr><td>482 Alder Crest Lane</td><td>Maple Heights</td><td>$ 1,200,000</td><td>4</td><td>2.5</td><td>1,814</td><td>$ 765</td><td>5</td></tr>
      <tr><td>482 Alder Crest Lane</td><td>Maple Heights</td><td>$ 1,200,000</td><td>4</td><td>2.5</td><td>1,814</td><td>$ 765</td><td>5</td></tr>
      <tr><td>482 Alder Crest Lane</td><td>Maple Heights</td><td>$ 1,200,000</td><td>4</td><td>2.5</td><td>1,814</td><td>$ 765</td><td>5</td></tr>
      <tr><td>482 Alder Crest Lane</td><td>Maple Heights</td><td>$ 1,200,000</td><td>4</td><td>2.5</td><td>1,814</td><td>$ 765</td><td>5</td></tr>
    </tbody>
  </table>
  <div class="scroll-track"><div class="scroll-thumb"></div></div>
</section>

<footer class="site-footer">
  Copyright © 2014 Company Name. All Rights Reserved.
  <div class="social"><span></span><span></span><span></span></div>
</footer>

</body>
</html>
```